Business Cards for Branding (Advertising) Agency

We need stylish and cool business cards.
Additional info:
1) Logo - see the attachment. You can use either the three penguins or just one penguin face (square or round) - at your discretion.
2) Text and other stuff for business card:
front side:
-Logo and company name: company name - Northern Herons - should be in English as is in logo. This is the only exception. The rest of the text will be in Russian.
-Who we are: Брендинговое агентство
-First and last name:
-Position: Управляющий партнёр
-Address:
-Phone:
-Email:
-Website:
Note: please don't use names of information fields, such as: who we are, first and last name, position, address, phone, email and website.

3) Our suggestions on design:
-The backside of the business card can be either blank or has something on it - at your discretion.
-The business card background should be either white or grey (you can use any tone of grey).

Additional Information:
1) БРЕНДИНГОВОЕ АГЕНТСТВО
2) ул. Верескова - these two words should be together on the same line
3) тел.: +7 (495) 381-60-92
моб.: +7 (916) 507-28-14

Reason: We would like to receive more stylish designs.

```html
<!DOCTYPE html>
<html lang="ru">
<head>
<meta charset="utf-8">
<title>Northern Herons — визитная карточка</title>
<link href="https://fonts.googleapis.com/css2?family=Roboto+Condensed:wght@300;400;700&display=swap" rel="stylesheet">
<style>
  :root {
    --bg: #e9e7e3;
    --paper: #ffffff;
    --paper-shade: #e4e5e7;
    --slate: #363e48;
    --ink: #1c1c1c;
    --muted: #7a7a7a;
    --orange: #f39a1e;
    --gold: #e9b21c;
    --light-text: #e6e8ea;
  }
  * { box-sizing: border-box; margin: 0; padding: 0; }
  html, body { width: 1200px; height: 900px; overflow: hidden; }
  body {
    background: var(--bg);
    font-family: "Roboto Condensed", Arial, sans-serif;
    display: flex;
    flex-direction: column;
    align-items: center;
    justify-content: center;
    gap: 48px;
  }
  .card {
    position: relative;
    width: 660px;
    height: 366px;
    background: var(--paper);
    box-shadow: 0 6px 18px rgba(0,0,0,.18);
    overflow: hidden;
  }

  /* Brand lockup */
  .brand {
    display: flex;
    align-items: center;
    gap: 14px;
  }
  .brand-dot {
    width: 34px; height: 34px;
    border-radius: 50%;
    background: var(--ink);
    flex: none;
  }
  .brand-name {
    font-weight: 300;
    font-size: 40px;
    letter-spacing: 2px;
    color: var(--ink);
    white-space: nowrap;
  }

  /* Face side */
  .card-face {
    display: flex;
    flex-direction: column;
    align-items: center;
    justify-content: center;
    gap: 14px;
  }
  .site-link {
    font-size: 20px;
    color: var(--orange);
    letter-spacing: .3px;
  }

  /* Contact side */
  .card-contact {
    background: linear-gradient(160deg, var(--paper) 35%, var(--paper-shade) 100%);
  }
  .contact-shape { position: absolute; inset: 0; }
  .card-contact .brand {
    position: absolute;
    left: 34px;
    top: 200px;
  }
  .card-contact .brand-name { font-size: 32px; }
  .card-contact .brand-dot { width: 28px; height: 28px; }
  .contact-info {
    position: absolute;
    left: 400px;
    top: 34px;
    right: 24px;
    bottom: 24px;
    color: var(--light-text);
  }
  .person-name {
    font-weight: 700;
    font-size: 22px;
    color: var(--orange);
  }
  .person-role {
    font-size: 13px;
    margin-top: 2px;
  }
  .contact-list {
    list-style: none;
    margin-top: 38px;
    font-size: 14px;
    line-height: 1.55;
  }
  .contact-list li { display: flex; align-items: center; gap: 7px; }
  .contact-list .address { padding-left: 21px; }
  .icon { width: 14px; height: 14px; flex: none; }
  .contact-site {
    position: absolute;
    left: 40px;
    bottom: 0;
    font-size: 17px;
    letter-spacing: .3px;
    white-space: nowrap;
  }
</style>
</head>
<body>

  <section class="card card-face" aria-label="Лицевая сторона визитки">
    <div class="brand">
      <span class="brand-dot"></span>
      <span class="brand-name">Northern Herons</span>
    </div>
    <p class="site-link">www.northernherons.ru</p>
  </section>

  <section class="card card-contact" aria-label="Оборотная сторона визитки">
    <svg class="contact-shape" viewBox="0 0 660 366" aria-hidden="true">
      <path d="M360 0 C 330 120 340 260 400 366 L 660 366 L 660 0 Z" fill="var(--slate)"/>
      <path d="M340 0 C 300 120 310 260 388 366 L 402 366 C 342 260 326 130 360 0 Z" fill="var(--gold)"/>
    </svg>

    <div class="brand">
      <span class="brand-dot"></span>
      <span class="brand-name">Northern Herons</span>
    </div>

    <div class="contact-info">
      <h1 class="person-name">Мария Соколова</h1>
      <p class="person-role">Управляющий партнёр</p>
      <ul class="contact-list">
        <li>
          <svg class="icon" viewBox="0 0 14 14" aria-hidden="true">
            <circle cx="7" cy="7" r="7" fill="var(--orange)"/>
            <path d="M4.3 3.6 L5.6 3.4 L6.2 5.1 L5.4 5.7 C5.9 6.8 6.8 7.7 7.9 8.2 L8.5 7.4 L10.2 8 L10 9.4 C7 9.6 4.1 6.7 4.3 3.6 Z" fill="var(--slate)"/>
          </svg>
          +7 (916) 507-28-14
        </li>
        <li>
          <svg class="icon" viewBox="0 0 14 14" aria-hidden="true">
            <circle cx="7" cy="7" r="7" fill="var(--orange)"/>
            <rect x="3.5" y="4.5" width="7" height="5" fill="none" stroke="var(--slate)" stroke-width="1"/>
            <path d="M3.5 4.5 L7 7.3 L10.5 4.5" fill="none" stroke="var(--slate)" stroke-width="1"/>
          </svg>
          maria@northernherons.ru
        </li>
        <li class="address">117246, г. Москва,</li>
        <li class="address">ул. Верескова, д.12, стр.2</li>
      </ul>
      <p class="contact-site">www.northernherons.ru</p>
    </div>
  </section>

</body>
</html>
```